Business Cards

Business cards (double-sided) to be handed out to clients and potential clients, with contact details, logo .

Target Market(s)

Small to medium size businesses

Industry/Entity Type

Accountants

Contact Information for Business Card

Brightwater Ledger & Counsel Ltd

Colors

Designer to choose only greyscale colors for use in the design.

Requirements
Must have
• Name, Title, Address, Phone number, Email, Website
Nice to have
• Modern, clean lines, classy
Should not have
• Business cards to be double-sided. Form keeps reverting to single-sided.

```html
<!DOCTYPE html>
<html lang="en">
<head>
<meta charset="utf-8">
<title>Brightwater Ledger &amp; Counsel – Business Card</title>
<link rel="stylesheet" href="https://fonts.googleapis.com/css2?family=Montserrat:wght@400;500&display=swap">
<style>
  :root {
    --backdrop: #d9d7d3;
    --card: #ffffff;
    --ink: #111111;
    --shadow: rgba(0, 0, 0, 0.35);
  }
  * { margin: 0; padding: 0; box-sizing: border-box; }
  html, body {
    width: 900px;
    height: 1200px;
    overflow: hidden;
    background: var(--backdrop);
    font-family: "Montserrat", sans-serif;
    color: var(--ink);
  }
  .canvas { position: relative; width: 900px; height: 1200px; }
  .card {
    position: absolute;
    left: 70px;
    width: 760px;
    height: 444px;
    background: var(--card);
    box-shadow: 0 4px 12px var(--shadow);
  }
  .card--front { top: 140px; }
  .card--back { top: 625px; }

  .wordmark {
    position: absolute;
    font-weight: 500;
    text-transform: uppercase;
    letter-spacing: 0.08em;
    line-height: 1.15;
    color: var(--ink);
  }
  .card--front .wordmark { left: 48px; top: 62px; font-size: 25px; }
  .card--back .wordmark {
    left: 0; right: 0; top: 172px;
    text-align: center;
    font-size: 30px;
  }

  .holder {
    position: absolute;
    right: 50px;
    top: 68px;
    text-align: right;
    text-transform: uppercase;
  }
  .holder__name { font-size: 27px; font-weight: 500; letter-spacing: 0.04em; }
  .holder__title { font-size: 16px; font-weight: 500; letter-spacing: 0.04em; margin-top: 4px; }

  .divider {
    position: absolute;
    left: 48px; right: 40px; top: 312px;
    height: 1.5px;
    background: var(--ink);
  }
  .contact {
    position: absolute;
    left: 48px; top: 324px;
    list-style: none;
    font-size: 17px;
  }
  .contact li { display: flex; align-items: center; height: 26px; }
  .contact svg { width: 18px; height: 16px; margin-right: 12px; fill: var(--ink); flex: none; }
  .address {
    position: absolute;
    right: 40px; top: 324px;
    text-align: right;
    font-size: 16px;
    font-style: normal;
    line-height: 26px;
  }
</style>
</head>
<body>
<div class="canvas">
  <section class="card card--front">
    <div class="wordmark">Brightwater Ledger<br>&amp; Counsel</div>
    <div class="holder">
      <p class="holder__name">Nora Ellison</p>
      <p class="holder__title">CEO/Founder</p>
    </div>
    <div class="divider"></div>
    <ul class="contact">
      <li>
        <svg viewBox="0 0 24 24" aria-hidden="true"><path d="M6.6 10.8a15.1 15.1 0 0 0 6.6 6.6l2.2-2.2c.3-.3.7-.4 1-.2 1.1.4 2.3.6 3.6.6.6 0 1 .4 1 1V20c0 .6-.4 1-1 1A17 17 0 0 1 3 4c0-.6.4-1 1-1h3.5c.6 0 1 .4 1 1 0 1.3.2 2.5.6 3.6.1.3 0 .7-.2 1z"/></svg>
        (372) 555-0148
      </li>
      <li>
        <svg viewBox="0 0 24 18" aria-hidden="true"><path d="M1 2h22v14H1z M2 3l10 7 10-7" stroke="#fff" stroke-width="1.5"/></svg>
        info@brightwaterledger.com
      </li>
      <li>
        <svg viewBox="0 0 24 24" aria-hidden="true"><g fill="none" stroke="#111" stroke-width="2"><circle cx="12" cy="12" r="10"/><ellipse cx="12" cy="12" rx="4.5" ry="10"/><path d="M2 12h20"/></g></svg>
        www.brightwaterledger.com
      </li>
    </ul>
    <address class="address">
      P.O. Box 417 2190 Alder Rd<br>
      Linwood Nebraska 20615
    </address>
  </section>

  <section class="card card--back">
    <div class="wordmark">Brightwater Ledger<br>&amp; Counsel</div>
  </section>
</div>
</body>
</html>
```